New ideas for home page of my website

I am looking for some inspiration for my website www.crafteddownriver.com
Most of the content will stay the same but I will be adding on the following new buttons Annual Expo and Awards
Any ideas on alternative layout act will be great. The most creative idea will get the opportunity to pitch for the whole site design.

Colors

Designer to choose colors to be used in the design.

```html
<!DOCTYPE html>
<html lang="en">
<head>
<meta charset="utf-8">
<title>Crafted Downriver – Home</title>
<link href="https://fonts.googleapis.com/css2?family=Bebas+Neue&family=Arimo:wght@400;700&display=swap" rel="stylesheet">
<style>
  :root {
    --page-bg: #e2e2e2;
    --panel: #ffffff;
    --ink: #222222;
    --muted: #666666;
    --accent: #c8102e;
    --accent-dark: #9e0c24;
    --nav-active: #111111;
    --caption-bg: rgba(20, 20, 20, 0.78);
    --rule: #cfcfcf;
  }
  * { box-sizing: border-box; margin: 0; padding: 0; }
  html, body { width: 1200px; height: 627px; overflow: hidden; }
  body {
    background: var(--page-bg);
    font-family: "Arimo", Arial, sans-serif;
    color: var(--ink);
  }
  .site { width: 900px; margin: 0 auto; height: 627px; overflow: hidden; }

  .site-header {
    height: 56px;
    display: flex;
    align-items: center;
    justify-content: space-between;
  }
  .brand { display: flex; align-items: center; gap: 9px; }
  .brand-dot { width: 30px; height: 30px; border-radius: 50%; background: var(--accent); }
  .brand-name {
    font-family: "Bebas Neue", "Arial Narrow", sans-serif;
    font-size: 26px;
    line-height: 1;
    color: var(--accent);
    letter-spacing: 0.5px;
  }
  .main-nav { display: flex; height: 34px; }
  .main-nav a {
    font-family: "Bebas Neue", "Arial Narrow", sans-serif;
    font-size: 14px;
    color: var(--ink);
    text-decoration: none;
    padding: 0 12px;
    display: flex;
    align-items: center;
    letter-spacing: 0.5px;
  }
  .main-nav a.is-active { background: var(--nav-active); color: #fff; }
  .main-nav a.is-new { color: var(--accent); }

  .hero { position: relative; height: 205px; }
  .hero-image {
    position: absolute; inset: 0;
    background: linear-gradient(180deg, #3d7fd4 0%, #79aee8 38%, #b9b4a8 55%, #7e7a72 78%, #4d4f4a 100%);
  }
  .hero-caption {
    position: absolute;
    left: 0; top: 62px;
    width: 330px;
    padding: 12px 16px;
    background: var(--caption-bg);
    color: #fff;
  }
  .hero-caption h2 {
    font-family: "Bebas Neue", "Arial Narrow", sans-serif;
    font-weight: 400;
    font-size: 24px;
    line-height: 1;
    margin-bottom: 7px;
  }
  .hero-caption p { font-size: 9.5px; line-height: 1.4; color: #e8e8e8; }
  .read-more {
    display: inline-block;
    margin-top: 8px;
    font-family: "Bebas Neue", "Arial Narrow", sans-serif;
    font-size: 13px;
    color: #fff;
    text-decoration: none;
    letter-spacing: 0.5px;
  }
  .slider-dots {
    position: absolute; right: 12px; bottom: 10px;
    display: flex; gap: 5px;
  }
  .slider-dots span { width: 7px; height: 7px; background: rgba(255,255,255,0.6); }
  .slider-dots span.is-current { background: #fff; }

  .tagline {
    margin-top: 8px;
    background: var(--panel);
    padding: 9px 16px;
    font-family: "Bebas Neue", "Arial Narrow", sans-serif;
    font-size: 15px;
    line-height: 1.3;
    letter-spacing: 0.3px;
  }

  .content { display: flex; gap: 8px; margin-top: 8px; height: 282px; }
  .panel { background: var(--panel); padding: 10px 12px; height: 100%; }
  .panel-title {
    font-family: "Bebas Neue", "Arial Narrow", sans-serif;
    font-weight: 400;
    font-size: 22px;
    line-height: 1;
    padding-bottom: 7px;
    border-bottom: 1px solid var(--rule);
    margin-bottom: 9px;
  }
  .featured { width: 234px; }
  .featured-photo {
    height: 96px;
    background: linear-gradient(135deg, #c9c4b6 0%, #8c8678 45%, #5d6a55 100%);
    margin-bottom: 9px;
  }
  .featured p { font-size: 8.5px; line-height: 1.45; color: var(--muted); }

  .members { flex: 1; display: flex; flex-direction: column; }
  .member-grid {
    display: grid;
    grid-template-columns: repeat(5, 1fr);
    gap: 10px 12px;
  }
  .member-thumb {
    height: 34px;
    background: radial-gradient(circle at 40% 40%, #7a1c2c 0%, #4a0f1b 70%, #2e0811 100%);
    margin-bottom: 5px;
  }
  .member-name {
    font-family: "Bebas Neue", "Arial Narrow", sans-serif;
    font-size: 12px;
    line-height: 1;
    margin-bottom: 3px;
  }
  .member-text { font-size: 8px; line-height: 1.4; color: var(--muted); }

  .feature-actions {
    margin-top: auto;
    display: flex;
    justify-content: flex-end;
    gap: 10px;
  }
  .feature-button {
    width: 120px;
    height: 24px;
    display: flex;
    align-items: center;
    justify-content: center;
    background: linear-gradient(180deg, var(--accent) 0%, var(--accent-dark) 100%);
    color: #fff;
    text-decoration: none;
    font-family: "Bebas Neue", "Arial Narrow", sans-serif;
    font-size: 13px;
    letter-spacing: 0.5px;
  }
</style>
</head>
<body>
<div class="site">
  <header class="site-header">
    <div class="brand">
      <span class="brand-dot"></span>
      <span class="brand-name">Crafted Downriver</span>
    </div>
    <nav class="main-nav">
      <a href="#" class="is-active">Home</a>
      <a href="#">Learn More</a>
      <a href="#">News</a>
      <a href="#">Events</a>
      <a href="#">Members</a>
      <a href="#" class="is-new">Annual Expo</a>
      <a href="#" class="is-new">Awards</a>
      <a href="#">Search</a>
    </nav>
  </header>

  <section class="hero">
    <div class="hero-image" role="img" aria-label="Photo of a modern theatre building with glass frontage under a blue sky"></div>
    <div class="hero-caption">
      <h2>Emphasized News</h2>
      <p>In feugiat nunc blandit varius consectetur adipiscing elit. Quam dolor non ultricies lorem. Aliquam porta scelerisque egestas. In mollis eros nec lacus laoreet et dapibus diam accumsan. Quam nunc non ultricies turpis nec ultrices metus.</p>
      <a href="#" class="read-more">... Read More</a>
    </div>
    <div class="slider-dots">
      <span></span><span></span><span></span><span></span><span class="is-current"></span>
    </div>
  </section>

  <p class="tagline">Sed sem purus, fermentum in porttitor quis, pharetra eu felis. Mauris at metus velit. In hac habitasse platea dictumst. Donec sem urna, semper in tristique eu, placerat eget justo.</p>

  <div class="content">
    <article class="panel featured">
      <h3 class="panel-title">Featured Article</h3>
      <div class="featured-photo" role="img" aria-label="Photo of two members standing in front of an exhibition banner"></div>
      <p>In feugiat nunc blandit varius consectetur adipiscing elit. Quam dolor non ultricies lorem. Aliquam porta scelerisque egestas. In mollis eros nec lacus laoreet et dapibus diam accumsan. Quam nunc non ultricies turpis nec ultrices metus.</p>
    </article>

    <section class="panel members">
      <h3 class="panel-title">Latest Members.</h3>
      <div class="member-grid">
        <div class="member"><div class="member-thumb" role="img" aria-label="Member photo"></div><div class="member-name">Lorem Ipsum</div><p class="member-text">Aliquam porta tortor nibh feugiat mollis eros.</p></div>
        <div class="member"><div class="member-thumb" role="img" aria-label="Member photo"></div><div class="member-name">Lorem Ipsum</div><p class="member-text">Aliquam porta tortor nibh feugiat mollis eros.</p></div>
        <div class="member"><div class="member-thumb" role="img" aria-label="Member photo"></div><div class="member-name">Lorem Ipsum</div><p class="member-text">Aliquam porta tortor nibh feugiat mollis eros.</p></div>
        <div class="member"><div class="member-thumb" role="img" aria-label="Member photo"></div><div class="member-name">Lorem Ipsum</div><p class="member-text">Aliquam porta tortor nibh feugiat mollis eros.</p></div>
        <div class="member"><div class="member-thumb" role="img" aria-label="Member photo"></div><div class="member-name">Lorem Ipsum</div><p class="member-text">Aliquam porta tortor nibh feugiat mollis eros.</p></div>
        <div class="member"><div class="member-thumb" role="img" aria-label="Member photo"></div><div class="member-name">Lorem Ipsum</div><p class="member-text">Aliquam porta tortor nibh feugiat mollis eros.</p></div>
        <div class="member"><div class="member-thumb" role="img" aria-label="Member photo"></div><div class="member-name">Lorem Ipsum</div><p class="member-text">Aliquam porta tortor nibh feugiat mollis eros.</p></div>
        <div class="member"><div class="member-thumb" role="img" aria-label="Member photo"></div><div class="member-name">Lorem Ipsum</div><p class="member-text">Aliquam porta tortor nibh feugiat mollis eros.</p></div>
        <div class="member"><div class="member-thumb" role="img" aria-label="Member photo"></div><div class="member-name">Lorem Ipsum</div><p class="member-text">Aliquam porta tortor nibh feugiat mollis eros.</p></div>
        <div class="member"><div class="member-thumb" role="img" aria-label="Member photo"></div><div class="member-name">Lorem Ipsum</div><p class="member-text">Aliquam porta tortor nibh feugiat mollis eros.</p></div>
      </div>
      <div class="feature-actions">
        <a href="#" class="feature-button">Annual Expo</a>
        <a href="#" class="feature-button">Awards</a>
      </div>
    </section>
  </div>
</div>
</body>
</html>
```